Detail Shop Business card design

i need a business card design for my new detailing company called 'Brenner's Detail Shop'. i want an all black and white design . simple, direct and to the point. i want the designer to choose a fitting font to match the logothe front should have logo, address, phone and email and the back side should have a slogan and text indicating that we offer services on anything including cars, trucks, motorcycles and RVs. slogan will read "we take pride in your ride"
maybe also very small on the back side the IG icon with Brenners_Detail_Shop

phone 482.615.7734
address 7384 E Harlow Ave
Spokane WA 99342
email: BrennersDetail@quorvail.com

Target Market(s)

all ages , auto enthusiasts

Industry/Entity Type

Automotive

Contact Information for Business Card

the front should have logo, address, phone and email and the back side should have a slogan and text indicating that we offer services on anything including cars, trucks, motorcycles and RVs. slogan will read "we take pride in your ride"

phone 482.615.7734
address 7384 E Harlow Ave
Spokane WA 99342

Colors
000000
ffffff

Requirements
Must have
• bold font and very simple design with good spacing
Nice to have
• anything creative from the designer indicating we service any types of vehicles
Should not have
• any colors ,

```html
<!DOCTYPE html>
<html lang="en">
<head>
<meta charset="utf-8">
<title>Brenner's Detail Shop — Business Cards</title>
<link rel="stylesheet" href="https://fonts.googleapis.com/css2?family=Arimo:wght@400;700&display=swap">
<style>
  :root {
    --bg: #9a9a9a;
    --ink: #111111;
    --card-dark: #1e1e1e;
    --card-light: #eeeeee;
    --paper-text: #ffffff;
    --shadow: rgba(0, 0, 0, 0.35);
  }
  * { margin: 0; padding: 0; box-sizing: border-box; }
  html, body {
    width: 1200px; height: 1200px; overflow: hidden;
    background: var(--bg);
    font-family: "Arimo", Arial, sans-serif;
  }
  .canvas { position: relative; width: 1200px; height: 1200px; }
  .card {
    position: absolute; left: 258px; width: 697px; height: 387px;
    box-shadow: 0 6px 14px var(--shadow);
  }
  .card--back { top: 158px; background: var(--card-dark); color: var(--paper-text); }
  .card--front { top: 629px; background: var(--card-light); color: var(--ink); }

  .brand {
    position: absolute; left: 0; right: 0; top: 112px;
    display: flex; flex-direction: column; align-items: center; gap: 14px;
  }
  .brand__mark {
    width: 54px; height: 54px; border-radius: 50%;
    border: 4px solid currentColor;
  }
  .brand__name {
    font-weight: 700; font-size: 32px; letter-spacing: 1px;
    text-transform: uppercase; line-height: 1;
  }

  .tagline {
    position: absolute; left: 0; right: 0; top: 330px;
    text-align: center; font-size: 13.5px; line-height: 1;
  }

  .contact__rule {
    position: absolute; left: 42px; right: 42px; top: 315px;
    height: 1px; background: var(--ink);
  }
  .contact {
    position: absolute; left: 42px; right: 42px; top: 330px;
    display: flex; justify-content: space-between; align-items: center;
    font-size: 13.5px; line-height: 1;
  }
  .contact__item { display: flex; align-items: center; gap: 7px; white-space: nowrap; }
  .contact__icon { width: 14px; height: 14px; fill: var(--ink); }
</style>
</head>
<body>
<main class="canvas">
  <section class="card card--back">
    <div class="brand">
      <span class="brand__mark"></span>
      <span class="brand__name">Brenner's Detail Shop</span>
    </div>
    <p class="tagline">We take pride in your ride</p>
  </section>

  <section class="card card--front">
    <div class="brand">
      <span class="brand__mark"></span>
      <span class="brand__name">Brenner's Detail Shop</span>
    </div>
    <div class="contact__rule"></div>
    <div class="contact">
      <span class="contact__item">
        <svg class="contact__icon" viewBox="0 0 16 16" aria-hidden="true">
          <path d="M1 5c0-2 3-3 7-3s7 1 7 3v1h-3V5H4v1H1z"/>
          <rect x="3" y="7" width="10" height="7" rx="1"/>
        </svg>
        482 615 7734
      </span>
      <span class="contact__item">
        <svg class="contact__icon" viewBox="0 0 16 16" aria-hidden="true">
          <path d="M1 3h14v10H1z"/>
          <path d="M2 4.2l6 4.8 6-4.8" fill="none" stroke="var(--card-light)" stroke-width="1.2"/>
        </svg>
        BrennersDetail@quorvail.com
      </span>
      <span class="contact__item">
        <svg class="contact__icon" viewBox="0 0 16 16" aria-hidden="true">
          <path d="M8 1a5 5 0 0 1 5 5c0 4-5 9-5 9S3 10 3 6a5 5 0 0 1 5-5zm0 3a2 2 0 1 0 0 4 2 2 0 0 0 0-4z" fill-rule="evenodd"/>
        </svg>
        7384 E Harlow Ave. Spokane, WA 99342
      </span>
    </div>
  </section>
</main>
</body>
</html>
```